REAL PSYCHIC rear window decal. Mystical, light, positive, spiritual coach vibes

Design a sign for my back car window.
HOT PINK and purple swirly, mystical sign. Eye-catching and classy.
Size 24” x 18”
TEXT:
MARISOL DEANE
Psychic & Medium
Www,.marisoldeane.com
World Renowned for Over 45 Years. (This last line make small at bottom)

*This is not a filled in magnet, it will be transparent.

Target Market(s)

Women

Industry/Entity Type

Spirituality

Font styles to use
Script
Other font styles liked:
• See upload for a font I like

Colors
E54698
E96AAD
F1A4CE
F9D9EA
FCEFF6
A7469A
B969AE
D3A5CF
EDDBEB
F8F0F9
6B429C
8869AF
B7A5CE
E3DAEB
F3F0F8

Requirements
Must have
• Pink purple, classy yet mystical vibe
Nice to have
• Easy to read, but old-timey classic font for “MARISOL DEANE”

```html
<!DOCTYPE html>
<html lang="en">
<head>
<meta charset="utf-8">
<title>Marisol Deane – Psychic &amp; Medium Window Decal</title>
<link rel="stylesheet" href="https://fonts.googleapis.com/css2?family=Pinyon+Script&family=Berkshire+Swash&family=Playfair+Display:wght@700&display=swap">
<style>
  :root {
    --hot-pink: #E54698;
    --blush: #F9D9EA;
    --royal-purple: #6B429C;
    --lavender: #8869AF;
    --soft-purple: #B969AE;
    --frame-grey: #BDBDBD;
    --paper: #FFFFFF;
  }
  html, body {
    margin: 0;
    padding: 0;
    width: 1200px;
    height: 1200px;
    overflow: hidden;
    background: var(--paper);
  }
  .decal {
    position: relative;
    width: 1200px;
    height: 1200px;
  }
  .decal__frame {
    position: absolute;
    left: 78px;
    top: 208px;
    width: 1044px;
    height: 784px;
    box-sizing: border-box;
    border: 1.5px solid var(--frame-grey);
  }
  .decal__name {
    position: absolute;
    left: 78px;
    top: 225px;
    width: 1044px;
    margin: 0;
    text-align: center;
    font-family: "Pinyon Script", cursive;
    font-weight: 400;
    font-size: 168px;
    line-height: 1.2;
    color: var(--hot-pink);
    white-space: nowrap;
  }
  .decal__eyes {
    position: absolute;
    left: 345px;
    top: 515px;
    width: 510px;
    height: 130px;
    border-radius: 65px 65px 30px 30px;
    background: linear-gradient(180deg, var(--blush) 0%, #B7A5CE 55%, var(--royal-purple) 100%);
  }
  .decal__arch {
    position: absolute;
    left: 0;
    top: 0;
    width: 1200px;
    height: 1200px;
  }
  .decal__title {
    font-family: "Berkshire Swash", cursive;
    font-size: 66px;
    fill: var(--royal-purple);
  }
  .decal__url {
    font-family: "Playfair Display", serif;
    font-weight: 700;
    font-size: 27px;
    letter-spacing: 1.5px;
    fill: var(--soft-purple);
  }
  .decal__tagline {
    position: absolute;
    left: 78px;
    top: 872px;
    width: 1044px;
    margin: 0;
    text-align: center;
    font-family: "Pinyon Script", cursive;
    font-size: 74px;
    line-height: 1.2;
    color: var(--lavender);
    white-space: nowrap;
  }
</style>
</head>
<body>
  <main class="decal">
    <div class="decal__frame"></div>

    <h1 class="decal__name">Marisol Deane</h1>

    <div class="decal__eyes" role="img" aria-label="Illustration of a pair of mystical eyes with pink and purple eyeshadow"></div>

    <svg class="decal__arch" viewBox="0 0 1200 1200" aria-hidden="false">
      <defs>
        <path id="title-curve" d="M 318 812 Q 600 700 882 812"/>
        <path id="url-curve" d="M 400 838 Q 600 790 800 838"/>
      </defs>
      <text class="decal__title" text-anchor="middle">
        <textPath href="#title-curve" startOffset="50%">Psychic &amp; Medium</textPath>
      </text>
      <text class="decal__url" text-anchor="middle">
        <textPath href="#url-curve" startOffset="50%">Www,.marisoldeane.com</textPath>
      </text>
    </svg>

    <p class="decal__tagline">World Renowned for Over 45 years</p>
  </main>
</body>
</html>
```